Business Cards & Stationary for Solo Attorney
Marcus Tolland Counsellor At Law
Business Cards & Stationary for Solo Attorney - Law
Creative Brief
Professional
Marcus Tolland
Counsellor At Law
482 Brindlecombe Avenue, 5th Floor Eastmere, Norland 08347
mtollandlaw@quillpost.example
tollandlawfirm.example

```html
<!DOCTYPE html>
<html lang="en">
<head>
<meta charset="utf-8">
<title>Marcus Tolland Counsellor At Law — Business Cards</title>
<link rel="stylesheet" href="https://fonts.googleapis.com/css2?family=Cinzel:wght@400;600&display=swap">
<style>
  :root {
    --navy: #1c2a5e;
    --navy-deep: #121c44;
    --navy-soft: #2b3a73;
    --paper: #ffffff;
    --paper-shade: #eef0f4;
    --ink: #1c2a5e;
    --silver: #d9dde8;
    --backdrop: #e4e5e8;
  }
  * { box-sizing: border-box; margin: 0; padding: 0; }
  html, body { width: 1200px; height: 901px; overflow: hidden; }
  body {
    background: var(--backdrop);
    font-family: "Cinzel", "Times New Roman", serif;
    position: relative;
  }
  .card {
    position: absolute;
    width: 640px;
    height: 366px;
    border-radius: 22px;
    overflow: hidden;
    box-shadow: 0 10px 28px rgba(0,0,0,0.18);
  }
  .card-back {
    left: 280px; top: 48px;
    background: linear-gradient(135deg, var(--navy-soft) 0%, var(--navy) 45%, var(--navy-deep) 100%);
    color: var(--silver);
    display: flex; flex-direction: column; align-items: center; justify-content: center;
  }
  .back-mark { display: flex; align-items: center; gap: 16px; }
  .back-mark .dot {
    width: 46px; height: 46px; border-radius: 50%;
    border: 2px solid var(--silver);
  }
  .back-mark .name {
    font-size: 30px; letter-spacing: 3px; font-weight: 400; text-transform: uppercase; white-space: nowrap;
  }
  .back-url {
    margin-top: 40px; font-size: 15px; letter-spacing: 6px; text-transform: uppercase;
  }
  .card-front {
    left: 280px; top: 486px;
    background: linear-gradient(160deg, var(--paper) 0%, var(--paper) 60%, var(--paper-shade) 100%);
    color: var(--ink);
  }
  .front-mark {
    position: absolute; left: 40px; top: 32px;
    text-align: center; width: 240px;
    font-weight: 400; text-transform: uppercase; color: var(--ink);
  }
  .front-mark .mark-name { font-size: 22px; letter-spacing: 1px; line-height: 1.1; white-space: nowrap; }
  .front-mark .mark-title { font-size: 11px; letter-spacing: 1.5px; margin-top: 4px; border-top: 1px solid var(--ink); display: inline-block; padding-top: 3px; }
  .holder { position: absolute; left: 48px; top: 112px; }
  .holder-name { font-size: 20px; letter-spacing: 1px; text-transform: uppercase; font-weight: 600; white-space: nowrap; }
  .holder-title { font-size: 11px; letter-spacing: 1.5px; text-transform: uppercase; margin-top: 4px; }
  .address {
    margin-top: 14px; font-size: 11px; letter-spacing: 1px; line-height: 1.5; text-transform: uppercase;
  }
  .contacts { list-style: none; margin-top: 10px; font-size: 11px; letter-spacing: 1px; text-transform: uppercase; }
  .contacts li { display: flex; align-items: center; gap: 8px; line-height: 1.55; white-space: nowrap; }
  .contacts svg { width: 13px; height: 13px; fill: var(--ink); flex: none; }
  .front-emblem {
    position: absolute; right: -110px; top: 70px;
    width: 330px; height: 330px; border-radius: 50%;
    background: var(--navy); opacity: 0.92;
  }
</style>
</head>
<body>
  <section class="card card-back">
    <div class="back-mark">
      <span class="dot"></span>
      <span class="name">Marcus Tolland</span>
    </div>
    <p class="back-url">www.tollandlawfirm.example</p>
  </section>

  <section class="card card-front">
    <div class="front-mark">
      <div class="mark-name">Marcus Tolland</div>
      <div class="mark-title">Counsellor At Law</div>
    </div>

    <div class="holder">
      <h1 class="holder-name">Marcus Tolland</h1>
      <p class="holder-title">Counsellor At Law</p>
      <p class="address">482 Brindlecombe Avenue<br>3rd Floor, Eastmere<br>Norland 08347</p>
      <ul class="contacts">
        <li><svg viewBox="0 0 16 16"><path d="M3 1h3l1 4-2 1.5c1 2 2.5 3.5 4.5 4.5L11 9l4 1v3c0 1-1 2-2 2C7 15 1 9 1 3c0-1 1-2 2-2z"/></svg>(555) 010-0148</li>
        <li><svg viewBox="0 0 16 16"><path d="M4 1h8v4H4zM1 6h14v7h-3v2H4v-2H1zM5 10v4h6v-4z"/></svg>(555) 010-0149</li>
        <li><svg viewBox="0 0 16 16"><path d="M1 3h14v10H1zM2.5 4.5 8 9l5.5-4.5v-.5h-11z"/></svg>mtollandlaw@quillpost.example</li>
        <li><svg viewBox="0 0 16 16"><circle cx="8" cy="8" r="6.5" fill="none" stroke="currentColor" stroke-width="1.5"/><path d="M1.5 8h13M8 1.5c2.5 2.5 2.5 10.5 0 13M8 1.5c-2.5 2.5-2.5 10.5 0 13" fill="none" stroke="currentColor" stroke-width="1.2"/></svg>tollandlawfirm.example</li>
      </ul>
    </div>

    <div class="front-emblem" role="img" aria-label="Large navy scales of justice decoration"></div>
  </section>
</body>
</html>
```